New Zealand Luggage Importer Needs Business Cards

We need professional, creative and fashionable business cards created.
We are based in New Zealand and import and distribute high-end, quality, fashionable and durable luggage.
We pride ourselves on selling the very best quality luggage, second only to 1 brand (which we won't mention here)...we use the same manufacturer. However, our prices are much more reasonable.
Industry/Entity Type
Business
Contact Information for Business Card
Mark Dunsley
027 512 4068
3/17 Harlow Street, Pinecrest Flats, Auckland, 0614
PO Box 204377, Fernside, Auckland 0731
09-528-3916
sales@brivancases.co.nz / www.brivancases.co.nz

```html
<!DOCTYPE html>
<html lang="en">
<head>
<meta charset="utf-8">
<title>Brivan Cases — Business Card and Luggage Tag</title>
<link rel="stylesheet" href="https://fonts.googleapis.com/css2?family=Arimo:wght@400;700&family=Oswald:wght@500&display=swap">
<style>
  :root {
    --backdrop: #161616;
    --card-dark: #232323;
    --card-light: #f1f1f1;
    --gold: #c9a24e;
    --ink: #151515;
    --ink-soft: #7a7a7a;
    --white: #ffffff;
  }
  * { margin: 0; padding: 0; box-sizing: border-box; }
  html, body { width: 1200px; height: 1001px; overflow: hidden; background: var(--backdrop); }
  body { position: relative; font-family: "Arimo", Arial, sans-serif; }

  .card { position: absolute; left: 317px; width: 567px; height: 318px; }
  .card-front { top: 154px; }
  .card-back { top: 528px; }
  .card-shape { position: absolute; inset: 0; width: 567px; height: 318px; }

  .brand { position: absolute; font-family: "Arimo", Arial, sans-serif; font-weight: 700; letter-spacing: 0.06em; text-transform: uppercase; white-space: nowrap; }
  .card-front .brand { left: 190px; top: 68px; font-size: 30px; color: var(--white); }
  .card-back .brand { left: 62px; top: 68px; font-size: 28px; color: var(--ink); }

  .contact-row { position: absolute; left: 36px; top: 232px; display: flex; align-items: center; gap: 14px; }
  .holder-name { font-family: "Oswald", "Arial Narrow", sans-serif; font-weight: 500; font-size: 29px; line-height: 1; color: var(--gold); text-transform: uppercase; white-space: nowrap; }

  .contact-list { list-style: none; font-size: 12.5px; color: var(--white); line-height: 18px; }
  .contact-list li { display: flex; align-items: center; gap: 7px; white-space: nowrap; }
  .contact-list svg { width: 10px; height: 11px; flex: none; }

  .postal { position: absolute; left: 62px; top: 108px; font-size: 13px; line-height: 19px; color: var(--ink); white-space: nowrap; }
  .if-found { position: absolute; left: 387px; top: 68px; font-family: "Oswald", "Arial Narrow", sans-serif; font-weight: 500; font-size: 34px; line-height: 43px; color: var(--ink-soft); text-transform: uppercase; }

  .field { position: absolute; left: 128px; display: flex; align-items: flex-end; gap: 6px; font-weight: 700; font-size: 17px; color: var(--ink); }
  .field-line { display: block; border-bottom: 1px solid var(--ink); height: 1px; margin-bottom: 4px; }
  .field-name { top: 190px; }
  .field-name .field-line { width: 314px; }
  .field-phone { top: 252px; }
  .field-phone .field-line { width: 296px; margin-left: 8px; }
</style>
</head>
<body>

<section class="card card-front" aria-label="Business card, front">
  <svg class="card-shape" viewBox="0 0 567 318" aria-hidden="true">
    <defs>
      <clipPath id="front-outline">
        <path d="M0 318 L0 150 C0 62 74 0 156 0 L567 0 L567 190 C567 262 508 318 427 318 Z"/>
      </clipPath>
      <linearGradient id="gold-band" x1="0" x2="1" y1="0" y2="0">
        <stop offset="0" stop-color="#a88434"/>
        <stop offset="0.55" stop-color="#dcb662"/>
        <stop offset="1" stop-color="#b9923f"/>
      </linearGradient>
    </defs>
    <g clip-path="url(#front-outline)">
      <rect width="567" height="318" fill="var(--card-dark)"/>
      <rect width="567" height="16" fill="url(#gold-band)"/>
    </g>
  </svg>
  <div class="brand">Brivan Cases</div>
  <div class="contact-row">
    <div class="holder-name">Mark Dunsley</div>
    <ul class="contact-list contact-phones">
      <li><svg viewBox="0 0 10 11"><rect x="2" y="0.5" width="6" height="10" rx="1" fill="none" stroke="var(--gold)" stroke-width="1.2"/></svg>027 512 4068</li>
      <li><svg viewBox="0 0 10 11"><path d="M2 1 L4 1 L5 3.5 L3.8 4.6 C4.5 6.2 5.3 7 6.6 7.7 L7.6 6.5 L10 7.5 L10 9.5 C10 10.2 9.4 10.6 8.6 10.5 C4.6 10 1 6.4 0.5 2.4 C0.4 1.6 1 1 2 1 Z" fill="var(--gold)"/></svg>09-528-3916</li>
    </ul>
    <ul class="contact-list contact-web">
      <li><svg viewBox="0 0 10 11"><rect x="0.5" y="2" width="9" height="7" fill="var(--gold)"/><path d="M0.5 2 L5 6 L9.5 2" fill="none" stroke="var(--card-dark)" stroke-width="1"/></svg>sales@brivancases.co.nz</li>
      <li><svg viewBox="0 0 10 11"><g fill="none" stroke="var(--gold)" stroke-width="0.9"><circle cx="5" cy="5.5" r="4.4"/><ellipse cx="5" cy="5.5" rx="2" ry="4.4"/><path d="M0.6 5.5 H9.4 M1.3 3.2 H8.7 M1.3 7.8 H8.7"/></g></svg>www.brivancases.co.nz</li>
    </ul>
  </div>
</section>

<section class="card card-back" aria-label="Luggage tag, back">
  <svg class="card-shape" viewBox="0 0 567 318" aria-hidden="true">
    <path d="M0 0 L419 0 C500 0 567 66 567 152 L567 318 L147 318 C66 318 0 252 0 168 Z" fill="var(--card-light)"/>
  </svg>
  <div class="brand">Brivan Cases</div>
  <p class="postal">3/17 Harlow Street, Pinecrest Flats, Auckland, 0614<br>PO Box 204377, Fernside, Auckland 0731</p>
  <div class="if-found">If Found<br>Contact</div>
  <div class="field field-name">NAME:<span class="field-line"></span></div>
  <div class="field field-phone">PHONE:<span class="field-line"></span></div>
</section>

</body>
</html>
```